BrightLoop Kiosk Business Card Design Project

BrightLoop Kiosk requires a business card design. We hire PhotoBooths to events such as Birthday Parties, Hens and Bucks Night, Anniversaries, Corporate Functions
, Engagements, Theme Nights, Presentation Night etc.
Business Card needs to look Modern, Professional And Catchy.
Updates

Hello Thankyou for all of your great designs, contact information will be provided shortly. We are considering the front of the card to be white themed and the back of the card to be black themed. And all social media colours to be their original colour. Thankyou

Hello everyone, Here are the contact details: Martin Colby - Manager Mobile number - 0491738205 Website - www.brightloopkiosk.example Email - admin@brightloopkiosk.example And if you can add the word "weddings" in the "We cater For" section would be good. Thankyou

Target Market(s)

Birthday Parties
Hens and Bucks Night
Weddings
Corporate Functions
Engagements
Theme Nights
Presentation Night
School Functions

Industry/Entity Type

Events

Requirements
Must have
• Must Match Logo
Must Have www.brightloopkiosk.example

On Back of card must have social media icons Facebook, Twitter, Youtube, Linkin and

We Cater For:

Birthday Parties
Hens and Bucks Night
Anniversaries
Corporate Functions
Engagements
Theme Nights
Presentation Night
School Functions
And more.....

```html
<!DOCTYPE html>
<html lang="en">
<head>
<meta charset="utf-8">
<title>BrightLoop Kiosk Business Card</title>
<link rel="stylesheet" href="https://fonts.googleapis.com/css2?family=Open+Sans:wght@400;600;700&display=swap">
<style>
  :root {
    --bg: #e4e2de;
    --card-white: #f7f7f7;
    --card-black: #0d0d0f;
    --brand-blue: #1ba3d6;
    --ink: #2a2a2a;
    --ink-soft: #5a5a5a;
    --rule: #3a3a3a;
    --list-text: #e8e8e8;
    --social: #4a4d55;
  }
  * { box-sizing: border-box; margin: 0; padding: 0; }
  html, body { width: 1200px; height: 1000px; overflow: hidden; }
  body {
    background: var(--bg);
    font-family: "Open Sans", Arial, sans-serif;
    position: relative;
  }
  .card {
    position: absolute;
    width: 540px;
    height: 315px;
    border-radius: 4px;
    box-shadow: 0 10px 28px rgba(0,0,0,0.22);
    overflow: hidden;
  }
  /* Front */
  .card-front { left: 50px; top: 150px; background: var(--card-white); }
  .front-edge {
    position: absolute; right: 0; top: 0; bottom: 0; width: 16px;
    background: var(--brand-blue);
  }
  .person {
    position: absolute; right: 62px; top: 58px; text-align: right;
  }
  .person-name { color: var(--brand-blue); font-size: 22px; font-weight: 400; }
  .person-role { color: var(--ink); font-size: 15px; font-weight: 600; margin-top: 2px; }
  .front-rule {
    position: absolute; right: 62px; top: 148px; width: 140px; height: 1px;
    background: var(--rule);
  }
  .brand { display: flex; align-items: center; gap: 12px; }
  .brand-mark { width: 22px; height: 22px; background: var(--brand-blue); }
  .brand-name { font-size: 26px; font-weight: 600; letter-spacing: 0.5px; }
  .card-front .brand { position: absolute; left: 40px; top: 120px; }
  .card-front .brand-name { color: var(--ink); }
  .contacts {
    position: absolute; left: 40px; bottom: 36px; list-style: none;
    font-size: 13px; color: var(--ink); line-height: 1.75;
  }
  .contacts li { display: flex; align-items: center; gap: 8px; }
  .contacts svg { width: 11px; height: 11px; fill: var(--brand-blue); flex: none; }
  .contacts .web { font-weight: 700; }

  /* Back */
  .card-back { left: 610px; top: 500px; background: var(--card-black); }
  .cater { position: absolute; left: 38px; top: 34px; }
  .cater-title { color: var(--brand-blue); font-size: 14px; font-weight: 700; margin-bottom: 4px; }
  .cater-list { list-style: none; color: var(--list-text); font-size: 14px; line-height: 1.42; }
  .cater-list li { display: flex; align-items: center; gap: 7px; }
  .cater-list svg { width: 11px; height: 11px; flex: none; }
  .cater-list .more { padding-left: 0; }
  .card-back .brand { position: absolute; right: 40px; top: 196px; }
  .card-back .brand-name { color: #ffffff; }
  .socials { position: absolute; right: 40px; top: 246px; display: flex; gap: 6px; }
  .socials span { width: 18px; height: 18px; border-radius: 3px; background: var(--social); }
</style>
</head>
<body>

<section class="card card-front" aria-label="Business card front">
  <div class="person">
    <p class="person-name">Martin Colby</p>
    <p class="person-role">Manager</p>
  </div>
  <div class="front-rule"></div>
  <div class="brand">
    <span class="brand-mark"></span>
    <span class="brand-name">BrightLoop Kiosk</span>
  </div>
  <ul class="contacts">
    <li><svg viewBox="0 0 12 12"><path d="M2.5 1l2 2-1 1.3c.7 1.5 1.7 2.5 3.2 3.2L8 6.5l2 2-1.2 1.8C5 10 2 7 1.7 2.2z"/></svg>0491738205</li>
    <li><svg viewBox="0 0 12 12"><path d="M1 2.5h10v7H1zM1.6 3l4.4 3.4L10.4 3"/></svg>admin@brightloopkiosk.example</li>
    <li class="web"><svg viewBox="0 0 12 12"><circle cx="6" cy="6" r="5"/></svg>www.brightloopkiosk.example</li>
  </ul>
  <div class="front-edge"></div>
</section>

<section class="card card-back" aria-label="Business card back">
  <div class="cater">
    <p class="cater-title">We Cater For:</p>
    <ul class="cater-list">
      <li><svg viewBox="0 0 12 12"><rect x="0.5" y="0.5" width="11" height="11" fill="none" stroke="#ccc"/><path d="M2.5 6l2.5 2.5L10 2" fill="none" stroke="#1ba3d6" stroke-width="2"/></svg>Birthday Parties</li>
      <li><svg viewBox="0 0 12 12"><rect x="0.5" y="0.5" width="11" height="11" fill="none" stroke="#ccc"/><path d="M2.5 6l2.5 2.5L10 2" fill="none" stroke="#1ba3d6" stroke-width="2"/></svg>Hens and Bucks Night</li>
      <li><svg viewBox="0 0 12 12"><rect x="0.5" y="0.5" width="11" height="11" fill="none" stroke="#ccc"/><path d="M2.5 6l2.5 2.5L10 2" fill="none" stroke="#1ba3d6" stroke-width="2"/></svg>Weddings</li>
      <li><svg viewBox="0 0 12 12"><rect x="0.5" y="0.5" width="11" height="11" fill="none" stroke="#ccc"/><path d="M2.5 6l2.5 2.5L10 2" fill="none" stroke="#1ba3d6" stroke-width="2"/></svg>Anniversaries</li>
      <li><svg viewBox="0 0 12 12"><rect x="0.5" y="0.5" width="11" height="11" fill="none" stroke="#ccc"/><path d="M2.5 6l2.5 2.5L10 2" fill="none" stroke="#1ba3d6" stroke-width="2"/></svg>Corporate Functions</li>
      <li><svg viewBox="0 0 12 12"><rect x="0.5" y="0.5" width="11" height="11" fill="none" stroke="#ccc"/><path d="M2.5 6l2.5 2.5L10 2" fill="none" stroke="#1ba3d6" stroke-width="2"/></svg>Engagements</li>
      <li><svg viewBox="0 0 12 12"><rect x="0.5" y="0.5" width="11" height="11" fill="none" stroke="#ccc"/><path d="M2.5 6l2.5 2.5L10 2" fill="none" stroke="#1ba3d6" stroke-width="2"/></svg>Theme Nights</li>
      <li><svg viewBox="0 0 12 12"><rect x="0.5" y="0.5" width="11" height="11" fill="none" stroke="#ccc"/><path d="M2.5 6l2.5 2.5L10 2" fill="none" stroke="#1ba3d6" stroke-width="2"/></svg>Presentation Night</li>
      <li><svg viewBox="0 0 12 12"><rect x="0.5" y="0.5" width="11" height="11" fill="none" stroke="#ccc"/><path d="M2.5 6l2.5 2.5L10 2" fill="none" stroke="#1ba3d6" stroke-width="2"/></svg>School Functions</li>
      <li class="more">And more.....</li>
    </ul>
  </div>
  <div class="brand">
    <span class="brand-mark"></span>
    <span class="brand-name">BrightLoop Kiosk</span>
  </div>
  <div class="socials" aria-label="Social media links">
    <span></span><span></span><span></span><span></span>
  </div>
</section>

</body>
</html>
```